Turn this into a clear and concise

Attached is a screen shot that we currently show to investors from a software program. We need you to illustrate this in a much more professional looking and easy to view and understand way. If we like your style and attention to detail there is more work behind this.
Industry/Entity Type
Software

```html
<!DOCTYPE html>
<html lang="en">
<head>
<meta charset="utf-8">
<title>Intra-day Countertrend US Hours — Example Trade</title>
<link rel="stylesheet" href="https://fonts.googleapis.com/css2?family=Source+Sans+3:wght@400;600;700&display=swap">
<style>
  :root{
    --page:#ffffff;
    --slate:#4b6276;
    --axis:#3c3c3c;
    --plot:#ffffff;
    --window:#d9dee4;
    --grid:#9a9a9a;
    --rule:#2b2b2b;
    --up:#8fc74a;
    --up-edge:#3d6b1e;
    --down:#d32f2f;
    --down-edge:#7a1515;
    --target:#f39c2b;
    --stop:#d8364a;
    --exit:#4a6fb5;
    --osc:#79c142;
    --osc-low:#7a5fa8;
    --osc-high:#f2a38a;
    --baseline:#8fd8d8;
    --volume:#2a4ea0;
    --time:#8dc63f;
    --ink:#ffffff;
    --label:#1d1d1d;
  }
  *{margin:0;padding:0;box-sizing:border-box}
  html,body{width:1200px;height:725px;overflow:hidden;background:var(--page)}
  body{position:relative;font-family:"Source Sans 3",Arial,sans-serif}
  .board{position:absolute;left:76px;top:56px;width:1040px;height:617px;background:var(--slate)}
  .board-title{position:absolute;left:0;right:0;top:76px;text-align:center;color:var(--ink);font-weight:700;font-size:15.5px;line-height:18px}
  .panel-heading{position:absolute;top:146px;width:408px;text-align:center;color:var(--ink);font-weight:700;font-size:12px;letter-spacing:.2px}
  .chart{position:absolute;top:177px;width:408px;height:439px;display:block}
  .entry{left:149px}
  .exit{left:621px}
  .chart text{font-family:"Source Sans 3",Arial,sans-serif}
  .axis-label{fill:var(--ink);font-weight:700;font-size:10px}
  .level-label{fill:var(--ink);font-weight:600;font-size:4.6px}
  .time-label{fill:var(--label);font-weight:700;font-size:9.5px;text-anchor:middle}
  .plot{fill:var(--plot)}
  .axis-strip{fill:var(--axis)}
  .window{fill:var(--window)}
  .grid{stroke:var(--grid);stroke-width:.5}
  .rule{stroke:var(--rule);stroke-width:.6}
  .stop-line{stroke:var(--stop);stroke-width:.9}
  .target-line{stroke:var(--target);stroke-width:.7;stroke-dasharray:2 1.5}
  .exit-line{stroke:var(--exit);stroke-width:.8;stroke-dasharray:2 1.5}
  .osc-low{stroke:var(--osc-low);stroke-width:.8}
  .osc-high{stroke:var(--osc-high);stroke-width:.8}
  .baseline{stroke:var(--baseline);stroke-width:.9}
  .osc-line{fill:none;stroke:var(--osc);stroke-width:2.2;stroke-linejoin:round}
  .wick{stroke:#333;stroke-width:.6}
  .up{fill:var(--up);stroke:var(--up-edge);stroke-width:.4}
  .down{fill:var(--down);stroke:var(--down-edge);stroke-width:.4}
  .vol rect{fill:var(--volume)}
  .signal{fill:var(--down);stroke:var(--down-edge);stroke-width:.4}
  .time-bar{fill:var(--time)}
</style>
</head>
<body>
<main class="board" aria-label="Example trade"></main>
<h1 class="board-title">Intra-day Countertrend US Hours<br>Example Trade: 30 year Treasury Bond, 7/13/14 “Payroll Friday”</h1>

<h2 class="panel-heading" style="left:149px">ENTRY (SELL)</h2>
<h2 class="panel-heading" style="left:621px">EXIT (BUY)</h2>

<!-- Entry chart -->
<svg class="chart entry" viewBox="0 0 306 329" role="img" aria-label="Entry chart: price, oscillator and volume">
  <rect class="plot" x="0" y="0" width="245" height="302"/>
  <rect class="axis-strip" x="245" y="0" width="61" height="302"/>
  <rect class="window" x="58" y="5" width="142" height="130"/>
  <g class="grid">
    <line x1="38" y1="0" x2="38" y2="302"/><line x1="110" y1="0" x2="110" y2="302"/>
    <line x1="169" y1="0" x2="169" y2="302"/><line x1="230" y1="0" x2="230" y2="302"/>
  </g>
  <line class="stop-line" x1="0" y1="15" x2="245" y2="15"/>
  <g class="target-line">
    <line x1="0" y1="29" x2="245" y2="29"/><line x1="0" y1="35" x2="245" y2="35"/>
    <line x1="0" y1="41" x2="245" y2="41"/><line x1="0" y1="48" x2="245" y2="48"/>
    <line x1="0" y1="55" x2="245" y2="55"/>
  </g>
  <g class="rule">
    <line x1="0" y1="68" x2="258" y2="68"/><line x1="0" y1="96" x2="258" y2="96"/>
    <line x1="0" y1="129" x2="258" y2="129"/><line x1="0" y1="135" x2="306" y2="135"/>
  </g>
  <text class="axis-label" x="262" y="19">137’24</text>
  <text class="level-label" x="255" y="30">137’20</text>
  <text class="level-label" x="255" y="36">137’18</text>
  <text class="level-label" x="255" y="42">137’16</text>
  <text class="level-label" x="255" y="49">137’14</text>
  <text class="level-label" x="255" y="56">137’12</text>
  <text class="axis-label" x="262" y="72">137’08</text>
  <text class="axis-label" x="262" y="100">136’28</text>
  <text class="axis-label" x="262" y="133">136’16</text>

  <g class="candles">
    <line class="wick" x1="18" y1="42" x2="18" y2="58"/><rect class="down" x="16" y="45" width="4" height="10"/>
    <line class="wick" x1="24" y1="50" x2="24" y2="57"/><rect class="down" x="22" y="52" width="4" height="3"/>
    <line class="wick" x1="30" y1="51" x2="30" y2="56"/><rect class="up" x="28" y="53" width="4" height="1.5"/>
    <line class="wick" x1="36" y1="51" x2="36" y2="56"/><rect class="up" x="34" y="53" width="4" height="1.5"/>
    <line class="wick" x1="42" y1="50" x2="42" y2="55"/><rect class="up" x="40" y="52" width="4" height="1.5"/>
    <line class="wick" x1="48" y1="49" x2="48" y2="56"/><rect class="down" x="46" y="51" width="4" height="3"/>
    <line class="wick" x1="54" y1="53" x2="54" y2="59"/><rect class="down" x="52" y="55" width="4" height="2"/>
    <line class="wick" x1="60" y1="55" x2="60" y2="62"/><rect class="down" x="58" y="57" width="4" height="3"/>
    <line class="wick" x1="66" y1="58" x2="66" y2="68"/><rect class="down" x="64" y="60" width="4" height="6"/>
    <line class="wick" x1="71" y1="64" x2="71" y2="82"/><rect class="down" x="69" y="66" width="4" height="14"/>
    <line class="wick" x1="77" y1="78" x2="77" y2="85"/><rect class="down" x="75" y="80" width="4" height="2"/>
    <line class="wick" x1="83" y1="83" x2="83" y2="104"/><rect class="down" x="81" y="85" width="4" height="15"/>
    <line class="wick" x1="89" y1="94" x2="89" y2="128"/><rect class="down" x="87" y="97" width="4" height="11"/>
    <line class="wick" x1="95" y1="97" x2="95" y2="112"/><rect class="up" x="93" y="100" width="4" height="8"/>
    <line class="wick" x1="100" y1="93" x2="100" y2="106"/><rect class="up" x="98" y="96" width="4" height="7"/>
    <line class="wick" x1="106" y1="92" x2="106" y2="101"/><rect class="up" x="104" y="95" width="4" height="3"/>
    <line class="wick" x1="112" y1="90" x2="112" y2="99"/><rect class="up" x="110" y="93" width="4" height="3"/>
    <line class="wick" x1="118" y1="88" x2="118" y2="97"/><rect class="up" x="116" y="91" width="4" height="3"/>
    <line class="wick" x1="124" y1="87" x2="124" y2="95"/><rect class="up" x="122" y="90" width="4" height="3"/>
    <line class="wick" x1="130" y1="87" x2="130" y2="95"/><rect class="down" x="128" y="90" width="4" height="2"/>
    <line class="wick" x1="136" y1="85" x2="136" y2="95"/><rect class="up" x="134" y="88" width="4" height="4"/>
    <line class="wick" x1="142" y1="83" x2="142" y2="93"/><rect class="up" x="140" y="86" width="4" height="4"/>
    <line class="wick" x1="148" y1="81" x2="148" y2="89"/><rect class="up" x="146" y="84" width="4" height="2"/>
    <line class="wick" x1="154" y1="73" x2="154" y2="88"/><rect class="up" x="152" y="76" width="4" height="9"/>
    <line class="wick" x1="159" y1="70" x2="159" y2="79"/><rect class="up" x="157" y="73" width="4" height="3"/>
    <line class="wick" x1="165" y1="71" x2="165" y2="79"/><rect class="down" x="163" y="74" width="4" height="2"/>
    <line class="wick" x1="171" y1="73" x2="171" y2="90"/><rect class="down" x="169" y="76" width="4" height="10"/>
    <line class="wick" x1="177" y1="79" x2="177" y2="89"/><rect class="up" x="175" y="82" width="4" height="4"/>
    <line class="wick" x1="183" y1="75" x2="183" y2="86"/><rect class="up" x="181" y="78" width="4" height="5"/>
    <line class="wick" x1="189" y1="73" x2="189" y2="81"/><rect class="up" x="187" y="76" width="4" height="2"/>
    <line class="wick" x1="195" y1="69" x2="195" y2="79"/><rect class="up" x="193" y="72" width="4" height="4"/>
    <line class="wick" x1="201" y1="63" x2="201" y2="75"/><rect class="up" x="199" y="66" width="4" height="6"/>
    <line class="wick" x1="207" y1="60" x2="207" y2="70"/><rect class="up" x="205" y="63" width="4" height="4"/>
    <line class="wick" x1="213" y1="60" x2="213" y2="67"/><rect class="down" x="211" y="63" width="4" height="1.5"/>
    <line class="wick" x1="219" y1="59" x2="219" y2="67"/><rect class="up" x="217" y="62" width="4" height="2"/>
    <line class="wick" x1="225" y1="53" x2="225" y2="65"/><rect class="up" x="223" y="56" width="4" height="6"/>
    <line class="wick" x1="231" y1="49" x2="231" y2="59"/><rect class="up" x="229" y="52" width="4" height="4"/>
    <line class="wick" x1="237" y1="50" x2="237" y2="56"/><rect class="up" x="235" y="52" width="4" height="1.5"/>
  </g>
  <path class="signal" d="M229 38h4v6h3l-5 6-5-6h3z"/>

  <line class="rule" x1="0" y1="141" x2="258" y2="141"/>
  <line class="grid" x1="0" y1="157" x2="245" y2="157"/>
  <line class="osc-low" x1="0" y1="205" x2="245" y2="205"/>
  <line class="baseline" x1="0" y1="232" x2="306" y2="232"/>
  <text class="axis-label" x="262" y="145">100</text>
  <text class="axis-label" x="262" y="224">o</text>
  <polyline class="osc-line" points="13,194 18,207 34,209 40,193 46,193 53,205 60,207 70,217 91,220 95,197 101,197 106,189 110,189 116,179 123,179 128,192 136,192 143,167 150,175 154,157 158,152 165,165 172,189 178,177 188,180 200,157 206,170 213,174 221,167 228,154 238,154"/>

  <line class="grid" x1="0" y1="241" x2="245" y2="241"/>
  <text class="axis-label" x="258" y="243">20,000</text>
  <text class="axis-label" x="258" y="266">10,000</text>
  <g class="vol">
    <rect x="2" y="282" width="3" height="20"/><rect x="7" y="277" width="3" height="25"/><rect x="12" y="284" width="3" height="18"/>
    <rect x="17" y="294" width="3" height="8"/><rect x="22" y="282" width="3" height="20"/><rect x="27" y="288" width="3" height="14"/>
    <rect x="32" y="296" width="3" height="6"/><rect x="37" y="290" width="3" height="12"/><rect x="42" y="290" width="3" height="12"/>
    <rect x="47" y="290" width="3" height="12"/><rect x="52" y="290" width="3" height="12"/><rect x="57" y="284" width="3" height="18"/>
    <rect x="62" y="277" width="3" height="25"/><rect x="67" y="290" width="3" height="12"/><rect x="72" y="240" width="3" height="62"/>
    <rect x="77" y="264" width="3" height="38"/><rect x="82" y="294" width="3" height="8"/><rect x="87" y="272" width="3" height="30"/>
    <rect x="92" y="272" width="3" height="30"/><rect x="97" y="290" width="3" height="12"/><rect x="102" y="296" width="3" height="6"/>
    <rect x="107" y="280" width="3" height="22"/><rect x="112" y="284" width="3" height="18"/><rect x="117" y="290" width="3" height="12"/>
    <rect x="122" y="296" width="3" height="6"/><rect x="127" y="290" width="3" height="12"/><rect x="132" y="292" width="3" height="10"/>
    <rect x="147" y="262" width="3" height="40"/><rect x="152" y="280" width="3" height="22"/><rect x="157" y="284" width="3" height="18"/>
    <rect x="162" y="288" width="3" height="14"/><rect x="167" y="290" width="3" height="12"/><rect x="172" y="288" width="3" height="14"/>
    <rect x="177" y="286" width="3" height="16"/><rect x="182" y="284" width="3" height="18"/><rect x="187" y="286" width="3" height="16"/>
    <rect x="192" y="288" width="3" height="14"/><rect x="197" y="282" width="3" height="20"/><rect x="202" y="288" width="3" height="14"/>
    <rect x="207" y="286" width="3" height="16"/><rect x="212" y="296" width="3" height="6"/><rect x="217" y="284" width="3" height="18"/>
    <rect x="222" y="288" width="3" height="14"/><rect x="227" y="288" width="3" height="14"/><rect x="232" y="284" width="3" height="18"/>
  </g>

  <rect class="time-bar" x="0" y="302" width="306" height="27"/>
  <text class="time-label" x="38" y="319">8am</text>
  <text class="time-label" x="110" y="319">9am</text>
  <text class="time-label" x="169" y="319">10am</text>
  <text class="time-label" x="230" y="319">11am</text>
</svg>

<!-- Exit chart -->
<svg class="chart exit" viewBox="0 0 306 329" role="img" aria-label="Exit chart: price, oscillator and volume">
  <rect class="plot" x="0" y="0" width="245" height="302"/>
  <rect class="axis-strip" x="245" y="0" width="61" height="302"/>
  <rect class="window" x="56" y="5" width="144" height="130"/>
  <g class="grid">
    <line x1="38" y1="0" x2="38" y2="302"/><line x1="110" y1="0" x2="110" y2="302"/>
    <line x1="169" y1="0" x2="169" y2="302"/><line x1="230" y1="0" x2="230" y2="302"/>
  </g>
  <g class="target-line">
    <line x1="0" y1="40" x2="245" y2="40"/><line x1="0" y1="45" x2="245" y2="45"/>
  </g>
  <line class="exit-line" x1="0" y1="57" x2="245" y2="57"/>
  <g class="rule">
    <line x1="0" y1="68" x2="258" y2="68"/><line x1="0" y1="96" x2="258" y2="96"/>
    <line x1="0" y1="129" x2="258" y2="129"/><line x1="0" y1="135" x2="306" y2="135"/>
  </g>
  <text class="axis-label" x="262" y="19">137’24</text>
  <text class="level-label" x="255" y="44">137’16</text>
  <text class="level-label" x="255" y="57">137’10</text>
  <text class="axis-label" x="262" y="72">137’08</text>
  <text class="axis-label" x="262" y="100">136’28</text>
  <text class="axis-label" x="262" y="133">136’16</text>

  <g class="candles">
    <line class="wick" x1="18" y1="42" x2="18" y2="58"/><rect class="down" x="16" y="45" width="4" height="10"/>
    <line class="wick" x1="24" y1="50" x2="24" y2="57"/><rect class="down" x="22" y="52" width="4" height="3"/>
    <line class="wick" x1="30" y1="51" x2="30" y2="56"/><rect class="up" x="28" y="53" width="4" height="1.5"/>
    <line class="wick" x1="36" y1="51" x2="36" y2="56"/><rect class="up" x="34" y="53" width="4" height="1.5"/>
    <line class="wick" x1="42" y1="50" x2="42" y2="55"/><rect class="up" x="40" y="52" width="4" height="1.5"/>
    <line class="wick" x1="48" y1="49" x2="48" y2="56"/><rect class="down" x="46" y="51" width="4" height="3"/>
    <line class="wick" x1="54" y1="53" x2="54" y2="59"/><rect class="down" x="52" y="55" width="4" height="2"/>
    <line class="wick" x1="60" y1="55" x2="60" y2="62"/><rect class="down" x="58" y="57" width="4" height="3"/>
    <line class="wick" x1="66" y1="58" x2="66" y2="68"/><rect class="down" x="64" y="60" width="4" height="6"/>
    <line class="wick" x1="71" y1="64" x2="71" y2="82"/><rect class="down" x="69" y="66" width="4" height="14"/>
    <line class="wick" x1="77" y1="78" x2="77" y2="85"/><rect class="down" x="75" y="80" width="4" height="2"/>
    <line class="wick" x1="83" y1="83" x2="83" y2="104"/><rect class="down" x="81" y="85" width="4" height="15"/>
    <line class="wick" x1="89" y1="94" x2="89" y2="128"/><rect class="down" x="87" y="97" width="4" height="11"/>
    <line class="wick" x1="95" y1="97" x2="95" y2="112"/><rect class="up" x="93" y="100" width="4" height="8"/>
    <line class="wick" x1="100" y1="93" x2="100" y2="106"/><rect class="up" x="98" y="96" width="4" height="7"/>
    <line class="wick" x1="106" y1="92" x2="106" y2="101"/><rect class="up" x="104" y="95" width="4" height="3"/>
    <line class="wick" x1="112" y1="90" x2="112" y2="99"/><rect class="up" x="110" y="93" width="4" height="3"/>
    <line class="wick" x1="118" y1="88" x2="118" y2="97"/><rect class="up" x="116" y="91" width="4" height="3"/>
    <line class="wick" x1="124" y1="87" x2="124" y2="95"/><rect class="up" x="122" y="90" width="4" height="3"/>
    <line class="wick" x1="130" y1="87" x2="130" y2="95"/><rect class="down" x="128" y="90" width="4" height="2"/>
    <line class="wick" x1="136" y1="85" x2="136" y2="95"/><rect class="up" x="134" y="88" width="4" height="4"/>
    <line class="wick" x1="142" y1="83" x2="142" y2="93"/><rect class="up" x="140" y="86" width="4" height="4"/>
    <line class="wick" x1="148" y1="81" x2="148" y2="89"/><rect class="up" x="146" y="84" width="4" height="2"/>
    <line class="wick" x1="154" y1="73" x2="154" y2="88"/><rect class="up" x="152" y="76" width="4" height="9"/>
    <line class="wick" x1="159" y1="70" x2="159" y2="79"/><rect class="up" x="157" y="73" width="4" height="3"/>
    <line class="wick" x1="165" y1="71" x2="165" y2="79"/><rect class="down" x="163" y="74" width="4" height="2"/>
    <line class="wick" x1="171" y1="73" x2="171" y2="90"/><rect class="down" x="169" y="76" width="4" height="10"/>
    <line class="wick" x1="177" y1="79" x2="177" y2="89"/><rect class="up" x="175" y="82" width="4" height="4"/>
    <line class="wick" x1="183" y1="75" x2="183" y2="86"/><rect class="up" x="181" y="78" width="4" height="5"/>
    <line class="wick" x1="189" y1="73" x2="189" y2="81"/><rect class="up" x="187" y="76" width="4" height="2"/>
    <line class="wick" x1="195" y1="69" x2="195" y2="79"/><rect class="up" x="193" y="72" width="4" height="4"/>
    <line class="wick" x1="201" y1="63" x2="201" y2="75"/><rect class="up" x="199" y="66" width="4" height="6"/>
    <line class="wick" x1="207" y1="63" x2="207" y2="70"/><rect class="down" x="205" y="65" width="4" height="2"/>
    <line class="wick" x1="213" y1="60" x2="213" y2="68"/><rect class="up" x="211" y="63" width="4" height="2"/>
    <line class="wick" x1="219" y1="57" x2="219" y2="67"/><rect class="up" x="217" y="60" width="4" height="4"/>
    <line class="wick" x1="225" y1="52" x2="225" y2="63"/><rect class="up" x="223" y="55" width="4" height="5"/>
    <line class="wick" x1="231" y1="50" x2="231" y2="58"/><rect class="up" x="229" y="52" width="4" height="3"/>
    <line class="wick" x1="237" y1="53" x2="237" y2="59"/><rect class="down" x="235" y="55" width="4" height="1.5"/>
  </g>
  <path class="signal" d="M215 36h4v6h3l-5 6-5-6h3z"/>

  <line class="baseline" x1="0" y1="133" x2="245" y2="133"/>
  <line class="rule" x1="0" y1="141" x2="258" y2="141"/>
  <line class="osc-high" x1="0" y1="156" x2="245" y2="156"/>
  <line class="osc-low" x1="0" y1="205" x2="245" y2="205"/>
  <line class="baseline" x1="0" y1="232" x2="306" y2="232"/>
  <text class="axis-label" x="262" y="145">100</text>
  <text class="axis-label" x="262" y="224">o</text>
  <polyline class="osc-line" points="14,204 22,204 26,189 31,187 37,200 46,202 54,212 72,219 79,192 86,189 91,189 97,175 104,175 110,187 118,187 124,172 131,167 137,154 143,152 149,165 157,179 164,184 174,172 184,164 191,159 196,172 204,167 211,162 219,155 227,160 237,167"/>

  <line class="grid" x1="0" y1="241" x2="245" y2="241"/>
  <text class="axis-label" x="258" y="243">20,000</text>
  <text class="axis-label" x="258" y="266">10,000</text>
  <g class="vol">
    <rect x="17" y="296" width="3" height="6"/><rect x="22" y="296" width="3" height="6"/><rect x="27" y="296" width="3" height="6"/>
    <rect x="32" y="296" width="3" height="6"/><rect x="37" y="296" width="3" height="6"/><rect x="42" y="294" width="3" height="8"/>
    <rect x="47" y="296" width="3" height="6"/><rect x="52" y="294" width="3" height="8"/><rect x="57" y="290" width="3" height="12"/>
    <rect x="62" y="282" width="3" height="20"/><rect x="67" y="264" width="3" height="38"/><rect x="72" y="234" width="3" height="68"/>
    <rect x="77" y="272" width="3" height="30"/><rect x="82" y="244" width="3" height="58"/><rect x="87" y="267" width="3" height="35"/>
    <rect x="92" y="290" width="3" height="12"/><rect x="97" y="287" width="3" height="15"/><rect x="102" y="277" width="3" height="25"/>
    <rect x="107" y="290" width="3" height="12"/><rect x="112" y="296" width="3" height="6"/><rect x="117" y="290" width="3" height="12"/>
    <rect x="122" y="280" width="3" height="22"/><rect x="127" y="280" width="3" height="22"/><rect x="132" y="296" width="3" height="6"/>
    <rect x="137" y="280" width="3" height="22"/><rect x="142" y="282" width="3" height="20"/><rect x="147" y="272" width="3" height="30"/>
    <rect x="152" y="294" width="3" height="8"/><rect x="157" y="278" width="3" height="24"/><rect x="162" y="280" width="3" height="22"/>
    <rect x="167" y="280" width="3" height="22"/><rect x="172" y="282" width="3" height="20"/><rect x="177" y="288" width="3" height="14"/>
    <rect x="182" y="287" width="3" height="15"/><rect x="187" y="290" width="3" height="12"/><rect x="192" y="282" width="3" height="20"/>
    <rect x="197" y="292" width="3" height="10"/><rect x="202" y="286" width="3" height="16"/><rect x="207" y="280" width="3" height="22"/>
    <rect x="212" y="268" width="3" height="34"/><rect x="217" y="272" width="3" height="30"/><rect x="222" y="282" width="3" height="20"/>
    <rect x="227" y="294" width="3" height="8"/><rect x="232" y="294" width="3" height="8"/>
  </g>

  <rect class="time-bar" x="0" y="302" width="306" height="27"/>
  <text class="time-label" x="38" y="319">8am</text>
  <text class="time-label" x="110" y="319">9am</text>
  <text class="time-label" x="169" y="319">10am</text>
  <text class="time-label" x="230" y="319">11am</text>
</svg>
</body>
</html>
```